Hypnotherapy- past life regression-life between lives therapist needs a website

I need a website that is enticing and spiritual in its feeling. It needs to have a lot of beautiful nature pictures included. The theme is "Quiet Harbor Path- what might you find....Lessons Solutions Answers"
Because all of us have the answers to living our best life, they are in our subconcious. But not everyone is capable of accessing them. Hypnosis accesses the subconcious and helps to create new neural pathways in the brain which can create new behaviors and responses to situations.
Hypnosis can help with anxiety, pain relief, weight loss, smoking/vaping cessation, self confidence......anything about yourself that you want to change.
Exploration of past lives and life between lives can reveal things related to ones current life. For example, perhaps your fear of deep water is a result of drowning in a past life. Once this has been discovered, it can lead to changes in ones current life.
Almost any personal behavior one wants to change, can be helped through hypnotherapy.
I need a page for testimonials, a place for scheduling (I will have a link to my scheduling app) some information about hypnotherapy.
I am uploading my logo files. My business card will be using the black and gold style, but my website does not have to reflect that. It can be based on the caramel and deep green like full color logo. Earthy, calm colors.
I also like the mock up of my logo on the beach and there was one on a starry night sky that I also liked.
Target Market(s)
men and women ages 25-50
Industry/Entity Type
natural health and wellness, spirituality
Number of Pages Required
4 page
Requirements
Must have
- a page for testimonials, perhaps with a beautiful nature picture with each one, I will have approximately 6. A link to schedule a complimentary intro session, preferably on the first page
Should not have
- no swinging watches or other sterotyped hypnosis symbols

```html
<!DOCTYPE html>
<html lang="en">
<head>
<meta charset="utf-8">
<title>Quiet Harbor Path – Hypnotherapy</title>
<link href="https://fonts.googleapis.com/css2?family=Cinzel:wght@400;500&family=Montserrat:wght@500;600;700&family=Roboto:ital,wght@0,400;0,500;1,400&display=swap" rel="stylesheet">
<style>
:root{
  --orange:#e4862b;
  --olive:#5b5a2a;
  --olive-dark:#4f4e24;
  --peach:#f4e0cc;
  --mist:#f5f5f4;
  --text:#777777;
  --ink:#333333;
  --white:#ffffff;
}
*{margin:0;padding:0;box-sizing:border-box}
html,body{width:1200px;height:3854px;overflow:hidden}
body{position:relative;background:var(--white);font-family:"Roboto",Arial,sans-serif;color:var(--text)}
.abs{position:absolute}
.btn{position:absolute;display:flex;align-items:center;justify-content:center;background:var(--orange);color:var(--white);border-radius:30px;font-family:"Montserrat",Arial,sans-serif;font-weight:700;text-transform:uppercase;text-decoration:none;white-space:nowrap}
.section-title{position:absolute;display:flex;align-items:center;justify-content:center;gap:14px;font-family:"Cinzel",Georgia,serif;color:var(--olive);font-size:46px;line-height:56px;font-weight:400;text-transform:uppercase;white-space:nowrap;left:0;width:1200px}
.section-title::before,.section-title::after{content:"";width:78px;height:3px;background:currentColor;flex:none}

/* hero */
.hero{left:0;top:0;width:1200px;height:700px;background:linear-gradient(160deg,#8a6e55 0%,#735843 40%,#5e4735 75%,#4f3c2e 100%)}
.brand{left:138px;top:40px;width:150px;text-align:center;color:var(--white);font-family:"Cinzel",Georgia,serif;font-size:19px;line-height:1.15}
.brand .mark{width:56px;height:56px;border-radius:50%;border:2px solid var(--white);margin:0 auto 8px}
.nav{font-family:"Montserrat",Arial,sans-serif;font-weight:500;font-size:16px;color:var(--white);text-transform:uppercase}
.nav a{color:inherit;text-decoration:none;position:absolute;white-space:nowrap}
.btn.login{left:947px;top:55px;width:108px;height:46px;font-size:17px}
.hero-title{left:300px;top:186px;width:600px;text-align:center;color:var(--white);font-family:"Cinzel",Georgia,serif;font-weight:400;font-size:34px;line-height:42px}
.btn.schedule{left:446px;top:341px;width:308px;height:45px;font-size:16px}
.dot{position:absolute;left:1126px;width:8px;height:8px;border-radius:50%;background:var(--white)}

/* about */
.about-art{left:140px;top:620px;width:400px;height:320px;border-radius:50%;background:radial-gradient(circle at 45% 50%,#f3e4d3 0%,#faf3ec 60%,#ffffff 100%);display:flex;align-items:center;justify-content:center;font-family:"Cinzel",Georgia,serif;color:var(--olive);font-size:26px}
.about-title{left:600px;width:auto;top:620px;justify-content:flex-start}
.about-title::before,.about-title::after{width:80px}
.about-copy{left:600px;top:690px;width:456px;font-size:14.5px;line-height:25.6px;text-align:justify}
.btn.read{left:600px;top:944px;width:133px;height:46px;font-size:14px}

/* services */
.services-title{top:1188px}
.ring{left:450px;top:1298px;width:300px;height:300px;border-radius:50%;border:5px solid var(--orange)}
.ring-center{left:525px;top:1380px;width:150px;height:130px;display:flex;align-items:center;justify-content:center;font-family:"Cinzel",Georgia,serif;font-size:15px;color:var(--olive);text-align:center;line-height:1.3}
.s-icon{position:absolute;width:72px;height:72px;border-radius:50%;border:3px solid var(--white);box-shadow:0 0 0 1px rgba(0,0,0,.05)}
.s-icon svg{width:100%;height:100%}
.svc{position:absolute;width:240px}
.svc h3{font-family:"Roboto",Arial,sans-serif;font-weight:500;font-size:18px;color:var(--ink);margin-bottom:12px}
.svc p{font-size:12.5px;line-height:20px}
.svc.right{text-align:right}
.svc.center{text-align:center;width:260px}

/* testimonials */
.test-title{top:2024px}
.t-card{position:absolute;top:2115px;width:301px;height:147px;border:2px solid #d8d8d8;background:var(--white);padding:22px 18px 0}
.t-card q{display:block;font-style:italic;font-size:10.5px;line-height:19px;color:#888;padding-right:10px}
.t-card .who{margin-top:10px;font-size:13px;color:var(--ink)}
.hexa{position:absolute;width:80px;height:90px;clip-path:polygon(50% 0,100% 25%,100% 75%,50% 100%,0 75%,0 25%)}
.stars{position:absolute;top:2276px;display:flex;gap:6px;font-size:15px}
.stars span{color:#f0b536}
.stars span.off{color:#5a4d3e}
.arrow{position:absolute;top:2172px;width:34px;height:34px;border-radius:50%;border:1.5px solid #555;display:flex;align-items:center;justify-content:center}
.btn.load{left:534px;top:2353px;width:132px;height:45px;font-size:14px}

/* blog */
.blog-title{top:2622px;color:var(--white)}
.post{position:absolute;top:2717px;width:282px;height:467px;background:var(--white);text-align:center}
.post .photo{position:absolute;left:5px;top:6px;width:272px;height:206px}
.post .date{position:absolute;left:66px;top:200px;width:150px;height:34px;border-radius:20px 20px 0 0;background:var(--white);display:flex;align-items:center;justify-content:center;gap:8px;font-family:"Montserrat",Arial,sans-serif;font-size:14px;color:var(--ink);font-weight:500}
.post .date i{width:18px;height:18px;border-radius:50%;background:var(--orange);display:inline-block}
.post h4{position:absolute;left:20px;right:20px;top:253px;font-family:"Roboto",Arial,sans-serif;font-weight:500;font-size:14px;line-height:21px;color:var(--ink);text-transform:uppercase}
.post p{position:absolute;left:22px;right:22px;top:303px;font-size:14.5px;line-height:21px}
.post .btn{left:72px;top:402px;width:138px;height:33px;font-size:12.5px}

/* footer */
.f-brand{left:500px;top:3335px;width:200px;text-align:center;font-family:"Cinzel",Georgia,serif;color:var(--orange);font-size:20px}
.f-brand .mark{width:60px;height:60px;border-radius:50%;border:2px solid var(--orange);margin:0 auto 10px}
.f-head{font-size:15px;color:var(--ink);font-weight:500}
.field{position:absolute;border:1px solid #d6d6d6;font-size:10.5px;color:#777;padding:8px 12px;text-transform:uppercase}
.btn.submit{left:609px;top:3701px;width:78px;height:27px;font-size:11.5px}
.c-row{position:absolute;left:759px;display:flex;align-items:center;gap:16px;font-size:11.5px;line-height:17px;color:#666}
.c-row .ic{width:30px;height:30px;border-radius:50%;flex:none;display:flex;align-items:center;justify-content:center}
.social{position:absolute;top:3688px;width:26px;height:26px;border-radius:50%}
.rule{left:132px;top:3779px;width:935px;height:1px;background:#d8d8d8}
.copy{left:0;top:3811px;width:1200px;text-align:center;font-size:12.5px;color:#444}
</style>
</head>
<body>

<!-- hero -->
<div class="abs hero" role="img" aria-label="Photograph of footsteps walking barefoot across wet beach sand"></div>
<svg class="abs" style="left:0;top:440px" width="1200" height="320" viewBox="0 0 1200 320" aria-hidden="true">
  <path d="M430,80 C560,20 700,10 820,30 C980,55 1120,140 1200,200 L1200,320 L430,320 Z" fill="var(--orange)"/>
  <path d="M0,228 C250,210 420,75 640,45 C820,22 1040,95 1200,225 L1200,320 L0,320 Z" fill="var(--white)"/>
</svg>

<div class="abs brand"><div class="mark"></div>QUIET HARBOR<br>PATH</div>
<nav class="abs nav" style="left:0;top:66px">
  <a style="left:362px">Home</a>
  <a style="left:453px">About</a>
  <a style="left:553px">Services</a>
  <a style="left:675px">Testimonials</a>
  <a style="left:836px">Contact</a>
</nav>
<a class="btn login">Login</a>
<h1 class="abs hero-title">QUIET HARBOR PATH- WHAT MIGHT YOU FIND....LESSONS SOLUTIONS ANSWERS</h1>
<a class="btn schedule">Schedule an appointment</a>
<span class="dot" style="top:330px"></span>
<span class="dot" style="top:346px;background:var(--orange)"></span>
<span class="dot" style="top:362px"></span>

<!-- about -->
<div class="abs about-art" role="img" aria-label="Large brand mark with footprints">Quiet Harbor Path</div>
<h2 class="section-title about-title">About Us</h2>
<p class="abs about-copy">Sed ut perspiciatis unde omnis iste natus error sit voluptatem accusantium doloremque laudantium, totam rem aperiam, eaque ipsa quae ab illo inventore veritatis et quasi architecto beatae vitae dicta sunt explicabo. Nemo enim ipsam voluptatem quia voluptas sit aspernatur aut odit aut fugit, sed quia consequuntur magni dolores eos qui ratione voluptatem sequi nesciunt. Neque porro quisquam est, qui dolorem ipsum quia dolor sit amet, consectetur, adipisci velit, sed quia non numquam eius modi tempora incidunt ut labore et dolore magnam aliquam quaerat voluptatem.</p>
<a class="btn read">Read more</a>

<!-- services -->
<svg class="abs" style="left:0;top:990px" width="1200" height="1000" viewBox="0 0 1200 1000" aria-hidden="true">
  <path d="M0,90 C200,40 400,20 650,60 C850,95 1000,40 1200,20 L1200,850 C1000,880 700,900 420,900 C250,900 120,870 0,860 Z" fill="var(--peach)"/>
  <path d="M0,100 C220,60 380,55 600,80 C820,105 1000,100 1200,60 L1200,930 C950,930 700,920 450,945 C300,960 120,930 0,880 Z" fill="var(--mist)"/>
  <path d="M0,860 C120,900 220,920 300,955 C200,980 100,990 0,990 Z" fill="var(--peach)"/>
</svg>
<h2 class="section-title services-title">Our Services</h2>

<div class="abs ring"></div>
<div class="abs ring-center" role="img" aria-label="Brand mark">Quiet Harbor<br>Path</div>

<div class="s-icon" style="left:455px;top:1300px;background:var(--olive)">
  <svg viewBox="0 0 72 72"><circle cx="36" cy="32" r="9" fill="none" stroke="#fff" stroke-width="2"/><path d="M22,54 C24,44 48,44 50,54" fill="none" stroke="#fff" stroke-width="2"/></svg>
</div>
<div class="s-icon" style="left:679px;top:1300px;background:var(--orange)">
  <svg viewBox="0 0 72 72"><path d="M30,22 L42,22 L42,36 L38,52 L34,52 L30,36 Z" fill="none" stroke="#fff" stroke-width="2"/><circle cx="45" cy="26" r="4" fill="none" stroke="#fff" stroke-width="2"/></svg>
</div>
<div class="s-icon" style="left:420px;top:1455px;background:var(--orange)">
  <svg viewBox="0 0 72 72"><path d="M24,24 L48,24 L48,48 L24,48 Z" fill="none" stroke="#fff" stroke-width="2"/><path d="M30,34 L42,34 M36,28 L36,40" stroke="#fff" stroke-width="2"/></svg>
</div>
<div class="s-icon" style="left:714px;top:1455px;background:var(--olive)">
  <svg viewBox="0 0 72 72"><circle cx="36" cy="36" r="14" fill="none" stroke="#fff" stroke-width="2"/><path d="M26,46 L46,26" stroke="#fff" stroke-width="2"/><rect x="28" y="34" width="16" height="4" fill="none" stroke="#fff" stroke-width="1.5"/></svg>
</div>
<div class="s-icon" style="left:564px;top:1566px;background:var(--olive)">
  <svg viewBox="0 0 72 72"><circle cx="36" cy="30" r="7" fill="none" stroke="#fff" stroke-width="2"/><path d="M24,52 C26,42 46,42 48,52 Z" fill="none" stroke="#fff" stroke-width="2"/><path d="M36,16 L36,19 M24,22 L26,24 M48,22 L46,24" stroke="#fff" stroke-width="2"/></svg>
</div>

<div class="svc right" style="left:188px;top:1305px"><h3>ANXIETY</h3><p>Sed ut perspiciatis unde omnis iste natus ecusantium doloremsantium doloremsantiuloremque</p></div>
<div class="svc" style="left:772px;top:1305px"><h3>PAIN RELIEF</h3><p>Sed ut perspiciatis unde omnis iste natus ecusantium doloremsantium doloremsantiuloremque</p></div>
<div class="svc right" style="left:153px;top:1459px"><h3>WEIGHT LOSS</h3><p>Sed ut perspiciatis unde omnis iste natus ecusantium doloremsantium doloremsantiuloremque</p></div>
<div class="svc" style="left:808px;top:1459px"><h3>SMOKING</h3><p>Sed ut perspiciatis unde omnis iste natus ecusantium doloremsantium doloremsantiuloremque</p></div>
<div class="svc center" style="left:470px;top:1652px"><h3>SELF CONFIDENCE</h3><p>Sed ut perspiciatis unde omnis iste natus ecusantium doloremed ut perspiciatis unde omnis iste natus ecusantium</p></div>

<!-- testimonials -->
<h2 class="section-title test-title">Testimonials</h2>
<div class="arrow" style="left:70px"><svg width="12" height="14" viewBox="0 0 12 14"><path d="M8,2 L3,7 L8,12" fill="none" stroke="#555" stroke-width="2"/></svg></div>
<div class="arrow" style="left:1094px"><svg width="12" height="14" viewBox="0 0 12 14"><path d="M4,2 L9,7 L4,12" fill="none" stroke="#555" stroke-width="2"/></svg></div>

<div class="t-card" style="left:130px"><q>Nemo enim ipsam voluptatem quia voluptas sit aspernatur aut odit aut fugit, sed quia consequuntur magni dolores eos qui ratione voluptatem sequi nesci-unt. Neque porro quisquam est.</q><div class="who">- John Doe</div></div>
<div class="t-card" style="left:450px"><q>Nemo enim ipsam voluptatem quia voluptas sit aspernatur aut odit aut fugit, sed quia consequuntur magni dolores eos qui ratione voluptatem sequi nesci-unt. Neque porro quisquam est.</q><div class="who">- John Doe</div></div>
<div class="t-card" style="left:769px"><q>Nemo enim ipsam voluptatem quia voluptas sit aspernatur aut odit aut fugit, sed quia consequuntur magni dolores eos qui ratione voluptatem sequi nesci-unt. Neque porro quisquam est.</q><div class="who">- John Doe</div></div>
<div class="hexa" style="left:332px;top:2220px;background:#c9b19c" role="img" aria-label="Portrait photo of a client"></div>
<div class="hexa" style="left:651px;top:2220px;background:#d7b49a" role="img" aria-label="Portrait photo of a client"></div>
<div class="hexa" style="left:971px;top:2220px;background:#b49a86" role="img" aria-label="Portrait photo of a client"></div>
<div class="stars" style="left:130px"><span>★</span><span>★</span><span>★</span><span class="off">★</span><span class="off">★</span></div>
<div class="stars" style="left:450px"><span>★</span><span>★</span><span>★</span><span class="off">★</span><span class="off">★</span></div>
<div class="stars" style="left:769px"><span>★</span><span>★</span><span>★</span><span class="off">★</span><span class="off">★</span></div>
<a class="btn load">Load more</a>

<!-- blog -->
<svg class="abs" style="left:0;top:2380px" width="1200" height="1020" viewBox="0 0 1200 1020" aria-hidden="true">
  <path d="M0,150 C250,150 420,190 620,110 C820,30 1000,20 1200,0 L1200,300 L0,300 Z" fill="var(--orange)"/>
  <path d="M0,110 C200,90 350,170 600,160 C850,150 1000,70 1200,110 L1200,880 C1000,860 850,950 600,920 C380,895 220,850 0,890 Z" fill="var(--olive)"/>
  <path d="M0,890 C220,850 380,895 600,920 C850,950 1000,860 1200,880 L1200,905 C1000,890 820,990 560,960 C320,935 180,990 0,990 Z" fill="var(--orange)"/>
</svg>
<h2 class="section-title blog-title">Blog Posts</h2>

<article class="post" style="left:142px">
  <div class="photo" role="img" aria-label="Photograph of a stressed woman holding her head with scribbled thoughts around her" style="background:linear-gradient(160deg,#d9dade,#a9aab0)"></div>
  <div class="date"><i></i>Jun 15,2021</div>
  <h4>Sed ut perspiciatis unde omnis iste natus</h4>
  <p>Lorem ipsum dolor sit amet, consectetur adipiscing elit, sed do eiusmod tempor incididunt ut labore et dolore magna aliqua.</p>
  <a class="btn">Learn more</a>
</article>
<article class="post" style="left:458px">
  <div class="photo" role="img" aria-label="Photograph of a waist being measured with a yellow tape" style="background:linear-gradient(180deg,#f2ece6 0%,#e4c9b2 45%,#1f4d52 60%,#173d42 100%)"></div>
  <div class="date"><i></i>Jun 15,2021</div>
  <h4>Sed ut perspiciatis unde omnis iste natus</h4>
  <p>Lorem ipsum dolor sit amet, consectetur adipiscing elit, sed do eiusmod tempor incididunt ut labore et dolore magna aliqua.</p>
  <a class="btn">Learn more</a>
</article>
<article class="post" style="left:773px">
  <div class="photo" role="img" aria-label="Photograph of a man casting a large strong shadow on a wall" style="background:linear-gradient(160deg,#8b8b8b,#4a4a4a)"></div>
  <div class="date"><i></i>Jun 15,2021</div>
  <h4>Sed ut perspiciatis unde omnis iste natus</h4>
  <p>Lorem ipsum dolor sit amet, consectetur adipiscing elit, sed do eiusmod tempor incididunt ut labore et dolore magna aliqua.</p>
  <a class="btn">Learn more</a>
</article>

<!-- footer -->
<div class="abs f-brand"><div class="mark"></div>QUIET HARBOR PATH</div>
<div class="abs" style="left:1070px;top:3370px;width:120px;height:420px;border-radius:60px;background:linear-gradient(180deg,rgba(228,134,43,.15),rgba(228,134,43,.35))" role="img" aria-label="Orange footprints walking up the page"></div>

<div class="abs f-head" style="left:143px;top:3494px">Schedule An Appointment</div>
<div class="field" style="left:145px;top:3534px;width:265px;height:29px">Name :</div>
<div class="field" style="left:422px;top:3534px;width:265px;height:29px">Phone :</div>
<div class="field" style="left:145px;top:3574px;width:542px;height:29px">Email :</div>
<div class="field" style="left:145px;top:3614px;width:542px;height:66px">Message :</div>
<a class="btn submit">Submit</a>

<div class="abs f-head" style="left:757px;top:3494px">Contact Information</div>
<div class="c-row" style="top:3535px">
  <span class="ic" style="border:1px solid #ddd"><svg width="12" height="16" viewBox="0 0 12 16"><path d="M6,15 C2,10 1,8 1,6 A5,5 0 0 1 11,6 C11,8 10,10 6,15 Z" fill="var(--orange)"/><circle cx="6" cy="6" r="2" fill="#fff"/></svg></span>
  <span>123,ed quia consequuntur magni dolores<br>eos qui ratione voluptatem sequi</span>
</div>
<div class="c-row" style="top:3583px">
  <span class="ic" style="background:var(--olive)"><svg width="14" height="14" viewBox="0 0 14 14"><path d="M3,1 L5,4 L4,6 C5,8 6,9 8,10 L10,9 L13,11 L12,13 C6,13 1,8 1,2 Z" fill="#fff"/></svg></span>
  <span>Phone : +1 555 014 2290</span>
</div>
<div class="c-row" style="top:3627px">
  <span class="ic" style="border:1px solid #ddd"><svg width="14" height="11" viewBox="0 0 14 11"><rect x="0.5" y="0.5" width="13" height="10" fill="var(--orange)"/><path d="M1,1 L7,6 L13,1" fill="none" stroke="#fff" stroke-width="1.3"/></svg></span>
  <span>info@quietharborpath.com</span>
</div>
<span class="social" style="left:761px;background:#3b5998" role="img" aria-label="Social profile"></span>
<span class="social" style="left:795px;background:#1da1f2" role="img" aria-label="Social profile"></span>
<span class="social" style="left:829px;background:#e62117" role="img" aria-label="Social profile"></span>
<span class="social" style="left:863px;background:#8a7a4a" role="img" aria-label="Social profile"></span>
<span class="social" style="left:897px;background:#0e76a8" role="img" aria-label="Social profile"></span>

<div class="abs rule"></div>
<p class="abs copy">Copyrights © 2023, Quiet Harbor Path. All Rights Reserved. &nbsp;|&nbsp; Privacy policy</p>

</body>
</html>
```